依頼詳細
上記に記載したアドバイスシートのベースを作成していただきたいです。内容は、顧客別に写真を入れたり、文字を入れたりするので、データで納品していただきたいです。30代、40代がメインターゲットで、おしゃれで少しラグジュアリーかつ女性らしいデザインを希望します。
内容や順番などこちらも変更する可能性があります。現在使っているアドバイスシートを参考にオシャレに、気分が上がるような仕上がりにしていただくのが希望です。 通常、初回の体験を受けていただいたお客様にはレッスンに進む方も多いのですが、こちらの方々にもノートというか、教科書のようなものを今後作成したいと思っているので、今回のデザインとも統一感を持たせたいと思っているので、お願いする可能性もあるかもしれません。
サイズ
A4
ページ数
10ページ
希望イメージ
シンプル 複雑
単色 カラフル
暗い 明るい
日常 高級
遊び心 厳粛
未来的 伝統的
女性的 男性的
希望する色
メイクアップと言って想像するような色、単色よりは数色使ってバランスの良い感じ
納品ファイル
補足説明
添付しているものが現在使用しているアドバイスシートです。これにもっと情報を追加していきたいので、添付しているものよりページ数などは増えると思います。(追加する文章や情報などは現在作成中です) 。デザインや、文字の配置、分かりやすさなどを追求したいので、そのあたりはアドバイスをいただけると有り難いです。現在、ベースのアドバイスシートをgood notesに取り込んで、iPadで文字と写真、写真への書き加えはペンで書き加えています。ですがこの作業が結構時間がかかって仕事量として重たいので、何かいいやり方があればそれもアドバイスいただけると嬉しいです。
内容は何度もやりとりして修正させていただく可能性があるので、一旦大幅であっても、早めに出していただけると決めやすいです。・最初のデザインの全体的な雰囲気や、ご提案者様の過去の事例など見させていただき雰囲気を決めさせていただきたいです。・あと、こちらからの希望になるべく沿っていただけるようやりとりしていただける方がとても有り難いです。当方今月より産休に入っており、日中も時間は割とあるので、ご対応していただけると助かります。(募集最終日頃にかなり決めた形で作り込んで応募される方よりは、最初はラフな形から今後柔軟に対応していただける方の方がありがたいです) 基本は作成枚数によって価格を決めさせていただきたいと思っています。現状より増える可能性が高いので、価格は上がる可能性があります。
ご応募ありがとうございます。追加修正の依頼を記載いたします。
【現在依頼しているページについて】
・ビフォーアフターや、各種メイク工程のページについて、文字量が多くみづらいのが難点で、もう少しグラフや表を入れて可視化したいです。(アイディアがあればお願いします) 添付PDF1枚目

【追加ページについて】
・お悩みとなりたいイメージを記載するページ(こちらも表やグラフなどで可視化できる案があればありがたいです)添付PDF2枚目

・添付PDF3枚目
利用サービスの流れを可視化できるページを作成したいです

・添付PDF4枚目
サロンの情報へアクセスできるよう情報をまとめたページ

今後メイクやスキンケア販売をしたい方へ向けての告知ページ

一旦以上になります。
すみません。募集が終了した場合添付ができないかもしれず、現在調べております。もしできない場合は、選定させていただき、個別にご連絡させていただきます。
可能な場合はPDF添付させていただきます。

依頼に加え、提案などしていただいたのでとても有り難かったです。

皆様とても魅力的なご提案ばかりで、ギリギリまで選定できず申し訳ございませんでした。今回は1社に決めさせていただいたのですが、素敵なご提案ばかりで、お願いして良かったなと思いました。こちらのご提案にお時間や尽力を割いていただいてありがとうございました。また機会ありましたらよろしくお願いいたします。

```html
<!DOCTYPE html>
<html lang="ja">
<head>
<meta charset="UTF-8">
<title>骨格分析 メイクアドバイスシート</title>
<link rel="stylesheet" href="https://fonts.googleapis.com/css2?family=Zen+Kaku+Gothic+New:wght@300;400&family=Parisienne&family=Noto+Serif+JP:wght@300;400&display=swap">
<style>
  :root {
    --rose: #d8899b;
    --rose-soft: #e3a6b3;
    --ink: #4a4446;
    --panel: #ffffff;
    --marble-a: #f7ece6;
    --marble-b: #efd9cf;
    --marble-c: #fbf5f1;
    --photo-a: #e9e7e6;
    --photo-b: #d6d3d2;
    --photo-c: #f3f1f0;
  }
  * { margin: 0; padding: 0; box-sizing: border-box; }
  html, body { width: 849px; height: 1200px; overflow: hidden; }
  body {
    background: #ffffff;
    font-family: "Zen Kaku Gothic New", sans-serif;
  }
  .sheet-cover {
    position: relative;
    width: 849px;
    height: 1200px;
    overflow: hidden;
    background:
      linear-gradient(125deg, var(--marble-c) 0%, var(--marble-a) 30%, var(--marble-b) 48%, var(--marble-c) 62%, var(--marble-a) 80%, var(--marble-b) 100%);
  }
  .cover-panel {
    position: absolute;
    left: 38px;
    top: 18px;
    width: 773px;
    height: 1146px;
    background: var(--panel);
    border-radius: 50% 50% 0 0 / 60px 60px 0 0;
    box-shadow: 0 0 0 1px rgba(216, 137, 155, 0.12);
  }
  .cover-title {
    position: absolute;
    top: 44px;
    width: 100%;
    text-align: center;
    color: var(--rose);
    font-weight: 300;
    font-size: 25px;
    letter-spacing: 0.22em;
  }
  .cover-subtitle {
    position: absolute;
    top: 86px;
    width: 100%;
    text-align: center;
    color: var(--rose-soft);
    font-weight: 300;
    font-size: 17px;
    letter-spacing: 0.62em;
  }
  .cover-photo {
    position: absolute;
    left: 72px;
    top: 228px;
    width: 630px;
    height: 296px;
    background:
      radial-gradient(circle at 72% 30%, var(--photo-c) 0%, transparent 40%),
      linear-gradient(135deg, var(--photo-a) 0%, var(--photo-b) 55%, var(--photo-a) 100%);
  }
  .cover-script {
    position: absolute;
    top: 578px;
    width: 100%;
    text-align: center;
    color: var(--rose);
    font-family: "Parisienne", cursive;
    font-size: 30px;
    letter-spacing: 0.2em;
  }
  .client-name {
    position: absolute;
    top: 634px;
    width: 100%;
    text-align: center;
    color: var(--rose);
    font-family: "Noto Serif JP", serif;
    font-weight: 300;
    font-size: 17px;
    letter-spacing: 0.18em;
  }
  .salon-mark {
    position: absolute;
    top: 1058px;
    width: 100%;
    display: flex;
    flex-direction: column;
    align-items: center;
    gap: 6px;
    color: var(--ink);
  }
  .salon-mark-row {
    display: flex;
    align-items: center;
    gap: 6px;
  }
  .salon-mark-dot {
    width: 8px;
    height: 8px;
    border-radius: 50%;
    background: var(--ink);
  }
  .salon-mark-name {
    font-size: 11px;
    font-weight: 400;
    letter-spacing: 0.12em;
  }
  .salon-mark-tag {
    font-size: 6px;
    letter-spacing: 0.2em;
  }
</style>
</head>
<body>
  <main class="sheet-cover">
    <section class="cover-panel">
      <h1 class="cover-title">骨格分析</h1>
      <p class="cover-subtitle">メイクアドバイスシート</p>
      <div class="cover-photo" role="img" aria-label="白い大理石の上に並ぶコスメ:チーク、リップ、ブラシ、ビューラー、クリームジャー"></div>
      <p class="cover-script">Make Advice Sheet</p>
      <p class="client-name">佐藤 美咲 様</p>
      <div class="salon-mark">
        <div class="salon-mark-row">
          <span class="salon-mark-dot"></span>
          <span class="salon-mark-name">LUMIERE ATELIER</span>
        </div>
        <span class="salon-mark-tag">MAKE SALON</span>
      </div>
    </section>
  </main>
</body>
</html>
```